bramblewood ridge livestock company website

we would like a home page, an about us page, a page for sires, a page for dams, A sale page where we can list progreny for sale and a contact us. on the about us page we would like there to be a family picture. on the sires page we would like to have a picture of each sire, a description beside them and a link to their online profile at prairie hereford. on the dam page we would like to have a picture of each dam, aswell as a description beside them aswell as a link to the prairie hereford site. would like the website to very mobile phone friendly as expecting most traffic to be on phone. we would like the website to look and feel very mich like a farm, rustic, barbed wire and other farm feels. we would also like a frozen genetics pages where we can include pictures and descriptions of the sires and dams aswell as a price for embryos and semen. we need to website to be easy to maintain so we can update pictures and information as it changes, we would like there to be a feature so that people can sign up to be on our mailing list by giving us their mailing addess and email and full name
aswell as an area where they can send us a message to contact us.

leaving for work for 3 weeks in the canadian arctic will have limited ability to use the internet

Target Market(s)

other ranchers, farmers, cattlemen,

Industry/Entity Type

farming, agriculture, cattle

Coding

Coded - Design and coding required

Requirements
Must have
• about page, contact page, sires page, dams page, SALE page.
Nice to have
• country/farm vibe, barbed wire, wood,

```html
<!DOCTYPE html>
<html lang="en">
<head>
<meta charset="utf-8">
<title>Bramblewood Ridge Livestock Company</title>
<link rel="stylesheet" href="https://fonts.googleapis.com/css2?family=Raleway:wght@300;400;600;700;800&family=Inter:wght@400;500;600;700&display=swap">
<style>
:root{
  --ink:#111111;
  --paper:#faf9f7;
  --white:#ffffff;
  --night:#000000;
  --grass-1:#6f8f3a;
  --grass-2:#4f7a25;
  --hill:#2c4a22;
  --hide:#9a4a1f;
  --barn:#4a3526;
  --barn-dark:#2d2019;
  --snow:#c9cdd2;
  --straw:#a89468;
  --accent:#c0262d;
  --icon:#888888;
}
*{margin:0;padding:0;box-sizing:border-box}
html,body{width:1200px;height:4342px;overflow:hidden}
body{position:relative;background:var(--white);color:var(--ink);font-family:"Inter",Arial,sans-serif}
.abs{position:absolute}

/* header */
.hero{left:0;top:0;width:1200px;height:922px;background:linear-gradient(180deg,var(--hill) 0%,#3d6a2a 22%,var(--grass-1) 45%,var(--grass-2) 100%)}
.hero-cows{left:0;top:260px;width:1200px;height:330px;background:radial-gradient(ellipse at 60% 50%,rgba(154,74,31,.85) 0%,rgba(154,74,31,.5) 40%,rgba(154,74,31,0) 70%)}
.header-shape{left:0;top:0}
.brand{left:40px;top:62px;width:240px;font-family:"Raleway",sans-serif;font-weight:800;font-size:25px;line-height:30px;color:var(--ink);text-transform:uppercase;text-align:center;letter-spacing:.5px}
.nav{top:43px;font-family:"Inter",Arial,sans-serif;font-weight:700;font-size:20px;color:var(--ink);letter-spacing:.3px;white-space:nowrap}
.social{top:25px;width:58px;height:58px;border-radius:50%;background:var(--ink)}
.hero-title{left:60px;top:398px;width:1080px;font-family:"Raleway",sans-serif;font-weight:300;font-size:70px;line-height:70px;color:var(--white);text-transform:uppercase;text-align:center;letter-spacing:1px}
.hero-btn{left:470px;top:637px;width:292px;height:62px;background:var(--night);color:var(--white);font-family:"Raleway",sans-serif;font-size:23px;letter-spacing:3px;line-height:62px;text-align:center}

/* welcome */
.welcome{left:0;top:922px;width:1200px;height:975px;background:var(--paper)}
.welcome-title{left:0;top:970px;width:1200px;font-family:"Raleway",sans-serif;font-weight:700;font-size:40px;line-height:49px;letter-spacing:3.5px;text-align:center;text-transform:uppercase}
.welcome-text{left:75px;top:1105px;width:1050px;font-size:25px;line-height:33.5px;text-align:center;color:var(--ink)}
.feature-photo{top:1358px;width:360px;height:361px}
.photo-snow{background:linear-gradient(180deg,var(--snow) 0%,#b8a99a 45%,var(--straw) 100%)}
.photo-field{background:linear-gradient(180deg,#5b8fcf 0%,#2f5a2c 25%,#6f9c3a 45%,#7aa83f 100%)}
.feature-title{top:1725px;width:520px;font-family:"Raleway",sans-serif;font-weight:700;font-size:37px;text-align:center;text-transform:uppercase}
.feature-text{top:1782px;width:420px;font-size:16.5px;line-height:22px;text-align:center}

/* cattle */
.products{left:0;top:1897px;width:1200px;height:1428px;background:var(--night)}
.products-title{left:0;top:1950px;width:1200px;font-family:"Raleway",sans-serif;font-weight:700;font-size:57px;letter-spacing:8px;color:var(--white);text-align:center}
.product-photo{width:394px;height:393px}
.tone-calves{background:linear-gradient(180deg,#9aa3a8 0%,#7a5038 55%,var(--straw) 100%)}
.tone-hanging{background:linear-gradient(180deg,#d9d6cf 0%,#8a4a2c 45%,#6d3a22 100%)}
.tone-pair{background:linear-gradient(180deg,#bdb8b2 0%,#7a3a1c 50%,#cfd3da 100%)}
.tone-stall{background:linear-gradient(180deg,#b28b5c 0%,#c9a676 50%,#a6875a 100%)}
.product-title{width:420px;font-family:"Raleway",sans-serif;font-weight:400;font-size:39px;letter-spacing:3px;color:var(--white);text-align:center;text-transform:uppercase}
.product-text{width:420px;font-size:24.5px;line-height:28px;color:var(--white);text-align:center}
.dot{top:3278px;width:17px;height:17px;border-radius:50%;background:var(--white)}
.dot.is-active{background:#555}

/* about */
.about{left:0;top:3325px;width:1200px;height:508px;background:linear-gradient(90deg,var(--barn-dark) 0%,var(--barn) 35%,#5a4331 55%,var(--barn) 75%,var(--barn-dark) 100%)}
.about-title{left:0;top:3440px;width:1200px;font-family:"Raleway",sans-serif;font-weight:700;font-size:57px;letter-spacing:11px;color:var(--white);text-align:center}
.about-text{left:130px;top:3548px;width:940px;font-size:25.5px;line-height:33.5px;color:var(--white);text-align:center}

/* footer */
.signup-title{left:0;top:3884px;width:1280px;font-weight:500;font-size:25px;text-align:center;text-transform:uppercase}
.signup-sub{left:0;top:3925px;width:1280px;font-weight:600;font-size:16.5px;text-align:center}
.email{left:393px;top:3977px;width:385px;height:35px;border:1px solid #999;font-size:16px;color:#555;padding-left:16px;line-height:33px}
.email-btn{left:778px;top:3977px;width:80px;height:35px;background:var(--accent)}
.agree{left:436px;top:4031px;font-size:19px;font-weight:500}
.agree-box{display:inline-block;width:21px;height:21px;border:2px solid #666;vertical-align:-4px;margin-right:10px;background:var(--white)}
.footer-brand{left:70px;top:4090px;width:300px;font-family:"Raleway",sans-serif;font-weight:800;font-size:28px;line-height:34px;text-transform:uppercase;text-align:center}
.col-head{top:4136px;font-weight:600;font-size:18px}
.col-list{top:4163px;font-size:17.5px;line-height:24px}
.hours{left:913px;top:4163px;width:270px;font-size:13px;line-height:20px}
.call{left:915px;top:4256px;width:101px;height:32px;background:var(--accent);color:var(--white);font-weight:700;font-size:17px;line-height:32px;text-align:center}
.copyright{left:0;top:4307px;width:1200px;font-size:19px;text-align:center}
</style>
</head>
<body>

<section class="abs hero" role="img" aria-label="Hereford cattle grazing in a green pasture below forested hills"></section>
<div class="abs hero-cows" role="img" aria-label="Red Hereford cows grazing tall grass"></div>

<svg class="abs header-shape" width="1200" height="280" viewBox="0 0 1200 280">
  <path d="M0 0H1200V96H392C318 96 282 140 230 190C190 228 120 250 0 266Z" fill="#faf9f7"/>
</svg>

<div class="abs brand">Bramblewood Ridge Livestock Company</div>

<nav>
  <span class="abs nav" style="left:385px">HOME</span>
  <span class="abs nav" style="left:470px">ABOUT US</span>
  <span class="abs nav" style="left:596px">SIRES</span>
  <span class="abs nav" style="left:684px">DAMS</span>
  <span class="abs nav" style="left:772px">SALE</span>
  <span class="abs nav" style="left:852px">CONTACT</span>
</nav>
<span class="abs social" style="left:959px"></span>
<span class="abs social" style="left:1030px"></span>
<span class="abs social" style="left:1100px"></span>

<h1 class="abs hero-title">Hereford seedstock<br>from our ranch to<br>your herd!</h1>
<div class="abs hero-btn">VIEW SALE CATTLE</div>

<section class="abs welcome"></section>
<h2 class="abs welcome-title">Welcome to<br>Bramblewood Ridge Livestock Company</h2>
<p class="abs welcome-text">We are a family-run Hereford seedstock ranch raising sound, fertile and easy-doing cattle for ranchers, farmers and cattlemen. Our herd is built on proven sires and strong maternal dams, bred for calving ease, good feet and mothering ability. Browse our sires and dams, see progeny listed for sale, or explore frozen genetics with embryos and semen available. Each animal links to its full online profile at Prairie Hereford so you can review pedigrees and records.</p>

<div class="abs feature-photo photo-snow" style="left:168px" role="img" aria-label="Herd sire standing on straw in the snow"></div>
<div class="abs feature-photo photo-field" style="left:676px" role="img" aria-label="Hereford cow grazing in a green pasture"></div>
<h3 class="abs feature-title" style="left:87px">Meet our sires</h3>
<h3 class="abs feature-title" style="left:600px">Meet our dams</h3>
<p class="abs feature-text" style="left:137px">Photos and descriptions of every herd sire, each with a link to his online profile at Prairie Hereford.</p>
<p class="abs feature-text" style="left:650px">Photos and descriptions of our cow herd, each with a link to her online profile at Prairie Hereford.</p>

<section class="abs products"></section>
<h2 class="abs products-title">OUR CATTLE</h2>

<div class="abs product-photo tone-calves" style="left:138px;top:2078px" role="img" aria-label="Herd sire resting on straw in winter"></div>
<div class="abs product-photo tone-hanging" style="left:689px;top:2077px" role="img" aria-label="Hereford cow standing in a corral"></div>
<div class="abs product-photo tone-pair" style="left:142px;top:2684px" role="img" aria-label="Cow with calf standing in snow"></div>
<div class="abs product-photo tone-stall" style="left:692px;top:2678px" role="img" aria-label="Young calf standing in a barn stall"></div>

<h3 class="abs product-title" style="left:127px;top:2476px">Sires</h3>
<p class="abs product-text" style="left:127px;top:2531px">Proven Hereford bulls selected for calving ease, growth and sound feet, with profiles at Prairie Hereford.</p>
<h3 class="abs product-title" style="left:678px;top:2476px">Dams</h3>
<p class="abs product-text" style="left:678px;top:2531px">Strong maternal cows with good udders and docile temperaments, each linked to her Prairie Hereford record.</p>
<h3 class="abs product-title" style="left:127px;top:3078px">Sale cattle</h3>
<p class="abs product-text" style="left:127px;top:3132px">Bulls, heifers and pairs from our program listed for sale, with photos, pedigrees and current pricing.</p>
<h3 class="abs product-title" style="left:681px;top:3076px">Frozen genetics</h3>
<p class="abs product-text" style="left:681px;top:3130px">Embryos and semen from our top sires and dams, with photos, descriptions and prices per unit.</p>

<span class="abs dot is-active" style="left:553px"></span>
<span class="abs dot" style="left:586px"></span>
<span class="abs dot" style="left:619px"></span>
<span class="abs dot" style="left:652px"></span>

<section class="abs about" role="img" aria-label="Family portrait in front of a wooden barn"></section>
<h2 class="abs about-title">ABOUT US</h2>
<p class="abs about-text">We are a ranch family raising registered Hereford cattle on the same ground our parents worked before us. Every calf is born, handled and fed by our family, and we stand behind the cattle we sell. Our goal is simple: breed practical, hardy Herefords that work for commercial and purebred producers alike. Come see the herd, call us with questions, or send a message anytime.</p>

<h2 class="abs signup-title">Join our mailing list</h2>
<p class="abs signup-sub">Sign up with your full name, email and mailing address for sale news, new genetics and ranch updates.</p>
<div class="abs email">Enter your email</div>
<div class="abs email-btn">
  <svg width="80" height="35" viewBox="0 0 80 35"><path d="M24 17.5H54M44 9L55 17.5L44 26" fill="none" stroke="#fff" stroke-width="3"/></svg>
</div>
<div class="abs agree"><span class="agree-box"></span>I agree to the Terms and Conditions</div>

<div class="abs footer-brand">Bramblewood Ridge Livestock Company</div>

<svg class="abs" style="left:232px;top:4186px" width="160" height="36" viewBox="0 0 160 36">
  <g fill="none" stroke="#888" stroke-width="2.5">
    <circle cx="18" cy="18" r="15"/><rect x="9" y="11" width="18" height="13"/><path d="M9 11L18 19L27 11"/>
  </g>
  <circle cx="65" cy="18" r="16" fill="#c0262d"/>
  <g fill="none" stroke="#888" stroke-width="2.5">
    <path d="M107 32C107 32 96 20 96 12A11 11 0 0 1 118 12C118 20 107 32 107 32Z"/><circle cx="107" cy="12" r="4"/>
    <circle cx="146" cy="18" r="15"/><path d="M139 11C139 20 145 27 153 26L154 22L149 20L147 22C144 21 142 18 142 16L144 14L142 9Z"/>
  </g>
</svg>

<h4 class="abs col-head" style="left:482px">Navigation</h4>
<div class="abs col-list" style="left:484px">Home<br>Sires<br>Dams</div>
<h4 class="abs col-head" style="left:703px">Quick Link</h4>
<div class="abs col-list" style="left:705px">Contact Us<br>Sale<br>About Us<br>Frozen Genetics<br>Mailing List</div>
<h4 class="abs col-head" style="left:913px;top:4139px">Work Hours</h4>
<p class="abs hours">Monday-Saturday xx am-xx pm<br>Visits to see the herd are welcome by appointment. Send a message and we will reply soon.</p>
<div class="abs call">Call us</div>

<p class="abs copyright">Copyright &nbsp;2026 bramblewood ridge livestock company. All rights reserved.</p>

</body>
</html>
```